Marlbrook Crest Healthcare Needs a Business Card Design

We need a business card design for a company based in Shorewood IL called "Marlbrook Crest Healthcare". We provide an integrated medical model involving chiropractic, trigger point injections and other medical services in one location. I have attached our logo to this with the colors being in the puzzle design of the logo. We are looking for a great design that will WOW those around us but also be able to communicate our information easily

Industry/Entity Type

Medical

Contact Information for Business Card

This is a integrated Medical office featuring numerous services to clients in the office.

Requirements
Must have
• Logo

```html
<!DOCTYPE html>
<html lang="en">
<head>
<meta charset="utf-8">
<title>Marlbrook Crest Healthcare – Business Card</title>
<link rel="stylesheet" href="https://fonts.googleapis.com/css2?family=Open+Sans:wght@400;600&display=swap">
<style>
  :root {
    --backdrop: #dcd7cf;
    --card-white: #f7f7f5;
    --sky-blue: #8fb6dc;
    --sky-blue-light: #a6c6e6;
    --brand-orange: #ec6f2d;
    --brand-blue: #4f82bf;
    --contact-text: #ffffff;
  }
  html, body {
    margin: 0;
    width: 1200px;
    height: 1023px;
    overflow: hidden;
    background: var(--backdrop);
    font-family: "Open Sans", Arial, sans-serif;
  }
  .canvas {
    position: relative;
    width: 1200px;
    height: 1023px;
  }
  .business-card {
    position: absolute;
    left: 100px;
    top: 221px;
    width: 1000px;
    height: 580px;
    background: var(--card-white);
    box-shadow: 0 10px 30px rgba(0, 0, 0, 0.18);
    overflow: hidden;
  }
  .card-shapes {
    position: absolute;
    inset: 0;
  }
  .brand-lockup {
    position: absolute;
    left: 195px;
    top: 378px;
    display: flex;
    align-items: center;
    gap: 14px;
  }
  .brand-square {
    flex: none;
    width: 44px;
    height: 44px;
    background: var(--brand-blue);
  }
  .brand-name {
    margin: 0;
    font-size: 24px;
    line-height: 32px;
    font-weight: 600;
    letter-spacing: 1px;
    color: var(--brand-blue);
    text-transform: uppercase;
  }
  .contact-block {
    position: absolute;
    left: 700px;
    top: 120px;
    width: 240px;
    text-align: right;
    color: var(--contact-text);
  }
  .contact-name {
    margin: 0 0 38px;
    font-size: 24px;
    font-weight: 600;
  }
  .contact-lines {
    margin: 0 0 26px;
    font-size: 15px;
    line-height: 24px;
  }
  .contact-web {
    margin: 0;
    font-size: 15px;
    line-height: 24px;
  }
</style>
</head>
<body>
<main class="canvas">
  <section class="business-card">
    <svg class="card-shapes" width="1000" height="580" viewBox="0 0 1000 580" aria-hidden="true">
      <defs>
        <linearGradient id="blueFill" x1="0" y1="0" x2="1" y2="1">
          <stop offset="0" stop-color="#8fb6dc"/>
          <stop offset="1" stop-color="#a6c6e6"/>
        </linearGradient>
      </defs>
      <path class="blue-panel" d="M665 0 Q 610 330 505 580 L1000 580 L1000 0 Z" fill="url(#blueFill)"/>
      <path class="swoosh-left" d="M0 470 Q 260 200 625 55 Q 280 240 0 500 Z" fill="var(--brand-orange)"/>
      <path class="swoosh-right" d="M625 55 Q 600 340 468 580 L442 580 Q 580 330 625 55 Z" fill="var(--brand-orange)"/>
    </svg>

    <div class="brand-lockup">
      <span class="brand-square"></span>
      <h1 class="brand-name">Marlbrook Crest<br>Healthcare</h1>
    </div>

    <div class="contact-block">
      <h2 class="contact-name">Name</h2>
      <p class="contact-lines">Address Line1<br>Address Line2<br>C&nbsp; 000000000<br>O&nbsp; 000000000</p>
      <p class="contact-web">email@marlbrookcrest.com<br>www.marlbrookcrest.com</p>
    </div>
  </section>
</main>
</body>
</html>
```